Business Card Design Project

Looking for a logo and business card for a Real State Business i will be opening. The name is not choosen yet , but will probably be RTV IMOVEIS.
I was thinking black and silver colors, but am open to nice ideas.
I did add a business card that i liked a lot, am looking for something like that, with logo in black or silver in a black card. The logo i was thinking in the letters RTV as i uploaded or something or little and cute buildings or a house...just ideas, can be any nice logo.
Updates

You guys can add other colors if you want, I like colors very "BRIGHT" and "open", like red, pink, strong colors. almost glow in the dark colors. lol

Designers,

I've increased more 88 dollars in the budget for 1st place cause I will want envelope designs... small and big sizes.

So 1st place is now U$248,00. 

No need to send the envelope designs right now... only the business cards designs.

Thank you.

Industry/Entity Type

Business

Requirements
Must have
• Renata Tavares Vilela

www.RTVimoveis-exemplo.com.br

+554188316402

renata@rtvimoveis-exemplo.com.br

```html
<!DOCTYPE html>
<html lang="pt-BR">
<head>
<meta charset="UTF-8">
<title>RTV IMOVEIS – Cartão de visita</title>
<link rel="stylesheet" href="https://fonts.googleapis.com/css2?family=Source+Sans+3:wght@400;600&display=swap">
<style>
  :root {
    --page-bg: #ffffff;
    --card-bg: #000000;
    --ink-light: #ffffff;
    --accent-pink: #e83ee3;
  }
  * { box-sizing: border-box; margin: 0; padding: 0; }
  html, body {
    width: 1056px;
    height: 1200px;
    overflow: hidden;
    background: var(--page-bg);
  }
  .business-card {
    position: absolute;
    left: 4px;
    top: 4px;
    width: 1048px;
    height: 1192px;
    background: var(--card-bg);
    border-radius: 64px;
    color: var(--ink-light);
    font-family: "Source Sans 3", "Myriad Pro", sans-serif;
    text-align: center;
  }
  .brand-mark {
    position: absolute;
    left: 50%;
    top: 196px;
    width: 220px;
    height: 220px;
    margin-left: -110px;
    border-radius: 50%;
    background: var(--accent-pink);
  }
  .brand-name {
    position: absolute;
    left: 0;
    right: 0;
    top: 477px;
    font-size: 128px;
    font-weight: 400;
    line-height: 1;
    letter-spacing: 1px;
    color: var(--ink-light);
    white-space: nowrap;
  }
  .agent-name {
    position: absolute;
    left: 0;
    right: 0;
    top: 683px;
    font-size: 50px;
    font-weight: 400;
    letter-spacing: 2.5px;
    white-space: nowrap;
  }
  .contact-list {
    position: absolute;
    left: 0;
    right: 0;
    top: 886px;
    list-style: none;
    font-size: 33px;
    line-height: 54px;
    white-space: nowrap;
  }
</style>
</head>
<body>
  <div class="business-card">
    <span class="brand-mark" aria-hidden="true"></span>
    <p class="brand-name">RTV IMOVEIS</p>
    <p class="agent-name">Renata Tavares Vilela</p>
    <ul class="contact-list">
      <li class="contact-web">www.RTVimoveis-exemplo.com.br</li>
      <li class="contact-phone">+554188316402</li>
      <li class="contact-email">renata@rtvimoveis-exemplo.com.br</li>
    </ul>
  </div>
</body>
</html>
```